The T.E.A.L. Program Display Poster

We need a design for a Display Poster (33"W x 73"H) for an expo we are attending May 9th.

Our website is www.tealprogramhub.org for more information

We are a 501(c)3 that works with youth who have been commercially sexual exploited. We have a California Licensed Therapeutic Residential Program, Drop-In Center and Thrift Store.

T.E.A.L. stands for Tenacious, Earnest, Adaptive and Lively

Our Full logo and Logo without Text is attached. Our mission is:
"Empowers youth to break away from Commercial Sexual Exploitation and Evolve from Victims to Leaders"

We want the design to highlight to phoenix logo, as well as indicate our mission statement.

The T.E.A.L. Program offers the following for youth who have been commercially sexually exploited:

• A California licensed (level 12) therapeutic residential program (WEAVING deep inside)
• A drop-in center (open 3pm-7pm Mondays through Fridays) (WEAVING onward)
• A Thrift Store where 100% of the proceeds benefit The T.E.A.L. Programming (WEAVING beyond)
The T.E.A.L. Program is:
• Survivor-Led
• Trauma Informed
• Strengths Based
• Culturally and Gender Responsive
• A model utilizing Harm Reduction coupled with Empowerment

Target Market(s)

Non-Profits, Possible Grant Organizations, Youth who have been commercially sexually exploited as children (CSEC)

Font styles to use
Serif

Colors
f68e4e
faa54b
fece3e
fbed22
9bcb3c
886aae
b768aa

Requirements
Must have
• Positive, empowering imagery.
Nice to have
• Inspiring imagery. want to inspire hope, strength, resilience
Should not have
• Negative, chains, imprisonment imagery

```html
<!DOCTYPE html>
<html lang="en">
<head>
<meta charset="utf-8">
<title>The T.E.A.L. Program Display Poster</title>
<link rel="stylesheet" href="https://fonts.googleapis.com/css2?family=Cabin:wght@400;600;700&family=Ubuntu:wght@700&display=swap">
<style>
  :root {
    --purple: #886aae;
    --purple-deep: #5b3b8c;
    --orchid: #b768aa;
    --green: #9bcb3c;
    --yellow: #fbed22;
    --gold: #fece3e;
    --amber: #faa54b;
    --orange: #f68e4e;
    --ink: #4a3a6a;
    --paper: #ffffff;
    --stage: #f2f2f2;
  }
  * { margin: 0; padding: 0; box-sizing: border-box; }
  html, body { width: 1200px; height: 900px; overflow: hidden; background: var(--stage); }
  .poster {
    position: absolute; left: 405px; top: 20px;
    width: 390px; height: 860px;
    background: var(--paper);
    overflow: hidden;
    box-shadow: 0 6px 24px rgba(0,0,0,.35);
    font-family: "Cabin", sans-serif;
    color: var(--ink);
  }
  .ribbons { position: absolute; inset: 0; }
  .brand {
    position: absolute; left: 24px; top: 95px; width: 342px;
    display: flex; align-items: center; gap: 14px;
  }
  .brand-mark {
    width: 130px; height: 130px; border-radius: 50%;
    background: var(--purple-deep); flex: none;
  }
  .brand-name {
    font-family: "Cabin", sans-serif; font-weight: 700;
    font-size: 34px; line-height: 1.05; color: var(--purple-deep);
  }
  .mission { position: absolute; left: 0; width: 100%; text-align: center; }
  .mission-empower { top: 448px; }
  .mission-evolve { top: 582px; }
  .mission-verb {
    font-family: "Ubuntu", sans-serif; font-weight: 700;
    font-size: 34px; letter-spacing: 1px; color: var(--orange);
    text-shadow: 1px 2px 0 #c4502a, 0 3px 6px rgba(0,0,0,.3);
  }
  .mission-line { font-size: 21px; line-height: 1.2; color: var(--ink); }
  .footer {
    position: absolute; left: 16px; right: 16px; bottom: 10px;
    text-align: center; color: var(--ink);
  }
  .offer { font-size: 6.2px; line-height: 7.6px; }
  .offer h3 { font-size: 6.6px; line-height: 7.8px; font-weight: 700; margin-bottom: 3px; }
  .offer ul { list-style: none; margin-bottom: 7px; }
  .offer li { white-space: nowrap; }
  .offer li::before { content: "• "; }
  .contact {
    margin-top: 6px;
    font-size: 8px; line-height: 10px; font-weight: 700; color: var(--purple-deep);
    white-space: nowrap;
  }
</style>
</head>
<body>
<main class="poster">
  <svg class="ribbons" viewBox="0 0 390 860" aria-hidden="true">
    <path fill="var(--yellow)" d="M260,0 H390 V380 C330,330 260,220 250,90 C248,50 252,20 260,0 Z"/>
    <path fill="var(--gold)" opacity=".7" d="M300,0 H390 V250 C340,200 300,120 300,0 Z"/>
    <path fill="var(--green)" d="M390,200 C320,260 220,340 180,450 C140,560 150,720 210,860 H110 C60,740 60,560 110,440 C170,310 290,230 390,170 Z"/>
    <path fill="var(--purple)" d="M0,0 H130 C40,140 60,300 190,410 C270,480 340,530 390,560 V860 H320 C300,720 230,580 90,500 C50,478 20,470 0,465 Z"/>
    <path fill="var(--orchid)" opacity=".35" d="M0,0 H70 C20,140 40,290 140,390 C80,380 30,360 0,340 Z"/>
    <path fill="var(--orange)" d="M390,300 C350,420 330,560 350,700 C358,760 370,820 390,860 Z"/>
    <path fill="var(--amber)" d="M150,860 C180,780 250,700 330,640 C300,720 280,800 290,860 Z"/>
    <path fill="var(--green)" d="M0,520 C50,600 80,700 70,860 H0 Z"/>
    <path fill="var(--purple)" d="M0,640 C30,720 40,800 30,860 H0 Z"/>
  </svg>

  <div class="brand">
    <span class="brand-mark" role="img" aria-label="Round program emblem area"></span>
    <span class="brand-name">The T.E.A.L. Program</span>
  </div>

  <section class="mission mission-empower">
    <div class="mission-verb">EMPOWERS</div>
    <p class="mission-line">youth to break away from<br>Commercial Sexual Exploitation</p>
  </section>
  <section class="mission mission-evolve">
    <div class="mission-verb">EVOLVE</div>
    <p class="mission-line">from Victims to Leaders</p>
  </section>

  <footer class="footer">
    <section class="offer">
      <h3>The T.E.A.L. Program offers the following<br>for youth who have been commercially sexually exploited:</h3>
      <ul>
        <li>A California licensed (level 12) therapeutic residential program (WEAVING deep inside)</li>
        <li>A drop-in center (open 3pm-7pm Mondays through Fridays) (WEAVING onward)</li>
        <li>A Thrift Store where 100% of the proceeds benefit The T.E.A.L. Programming (WEAVING beyond)</li>
      </ul>
      <h3>The T.E.A.L. Program is:</h3>
      <ul>
        <li>Survivor-Led</li>
        <li>Trauma Informed</li>
        <li>Strengths Based</li>
        <li>Culturally and Gender Responsive</li>
        <li>A model utilizing Harm Reduction coupled with Empowerment</li>
      </ul>
    </section>
    <p class="contact">The T.E.A.L. Program hello@tealprogramhub.org &nbsp;or&nbsp; Call us 555.301.487</p>
  </footer>
</main>
</body>
</html>
```